Lotuvan Cafe Menu rev.01

Design an elegant menu for Khmer restaurant in Melbourne.

-Size and format can be proposed (not bigger than A3)
-Food and beverages split (separate sides of the menu)
-Sample excel file - Food attached
-Sample Menu Pdf attached (just to get an idea)
-Details shall be reviewed and considered
-Prices in AUD
-Easy to print and clean (format need to to printable)
-Provision for future updates.

If you have any further question please let us know.
Regards,

Dexter

Target Market(s)

Customers win the restaurant

Industry/Entity Type

Hospitality - Restaurant

Colors

Designer to choose colors to be used in the design.

Requirements
Must have
• Authentic touch - clear structure
Nice to have
• Welcome about the restaurant. Complete information - see sample menu

```html
<!DOCTYPE html>
<html lang="en">
<head>
<meta charset="utf-8">
<title>Lotuvan Cafe Menu</title>
<link href="https://fonts.googleapis.com/css2?family=Montserrat:wght@400;500;700;800&family=Courier+Prime&display=swap" rel="stylesheet">
<style>
  :root {
    --canvas: #f3f3f3;
    --board: #343434;
    --board-dark: #262626;
    --cover: #2a2a2a;
    --gold: #c9b98a;
    --gold-soft: #a99d78;
    --ink-light: #e9e6dc;
    --muted: #9a9a94;
    --legend-bg: #ececec;
    --veg: #8bc34a;
    --vegan: #2e8b57;
    --gf: #f0a030;
    --spicy: #d9342b;
  }
  * { box-sizing: border-box; margin: 0; padding: 0; }
  html, body { width: 1200px; height: 1200px; overflow: hidden; }
  body {
    background: var(--canvas);
    font-family: "Montserrat", Arial, sans-serif;
    position: relative;
  }
  .page {
    position: absolute;
    top: 338px;
    width: 370px;
    height: 524px;
    overflow: hidden;
    background: radial-gradient(ellipse at 60% 40%, #3d3d3d 0%, var(--board) 55%, var(--board-dark) 100%);
    box-shadow: 0 6px 18px rgba(0,0,0,.25);
  }
  .page--left { left: 30px; }
  .page--right { left: 400px; box-shadow: 6px 6px 18px rgba(0,0,0,.25); }
  .page--cover { left: 800px; background: var(--cover); }

  .photo {
    position: absolute;
    border-radius: 50%;
    border: 3px solid #f4f4f4;
    outline: 1px dotted var(--gold-soft);
    outline-offset: 6px;
  }
  .photo--dessert { left: -55px; top: -35px; width: 190px; height: 190px;
    background: radial-gradient(circle at 55% 45%, #e8dcc0 0%, #3a7fb8 45%, #1c4f86 100%); }
  .photo--chicken { left: 202px; top: 197px; width: 136px; height: 136px;
    background: radial-gradient(circle at 50% 50%, #c77a3e 0%, #d89b5c 40%, #f2f2f2 72%); }
  .photo--salad { left: -65px; top: 325px; width: 190px; height: 190px;
    background: radial-gradient(circle at 55% 50%, #a57a4a 0%, #5e9e3f 45%, #f6f6f6 75%); }
  .photo--herbs { left: 0; top: 430px; width: 160px; height: 160px;
    background: radial-gradient(circle at 50% 40%, #7fa64b 0%, #b7a07a 50%, #3f7a58 100%); }

  .section { position: absolute; }
  .section__title {
    font-weight: 800; font-size: 8.5px; letter-spacing: 1.2px;
    color: var(--ink-light); text-transform: uppercase; text-align: center;
    margin-bottom: 5px;
  }
  .section__rule { height: 1px; background: var(--gold-soft); margin-top: 6px; opacity: .7; }
  .item { display: flex; justify-content: space-between; align-items: flex-start; margin-bottom: 4px; }
  .item__name { font-weight: 700; font-size: 8.5px; color: var(--gold); line-height: 1.15; }
  .item__desc { font-size: 4.6px; color: var(--muted); line-height: 1.3; max-width: 150px; }
  .item__price { font-weight: 700; font-size: 8px; color: var(--gold); padding-left: 8px; white-space: nowrap; }

  .tasty { left: 170px; top: 28px; width: 188px; }
  .breakfast { left: 14px; top: 170px; width: 186px; }
  .house { left: 148px; top: 338px; width: 212px; }
  .grill { left: 14px; top: 28px; width: 262px; }
  .salads { left: 14px; top: 210px; width: 262px; }
  .sides { left: 14px; top: 320px; width: 200px; }

  .legend {
    position: absolute; left: 96px; top: 494px; width: 274px; height: 20px;
    background: var(--legend-bg); display: flex; align-items: center; gap: 10px; padding: 0 8px;
    font-family: "Courier Prime", "Courier New", monospace; font-size: 8px; color: #444;
  }
  .legend__item { display: flex; align-items: center; gap: 3px; }
  .legend__dot { width: 10px; height: 10px; border-radius: 50%; color: #fff;
    font-family: "Montserrat", Arial, sans-serif; font-size: 4.5px; font-weight: 700;
    display: flex; align-items: center; justify-content: center; }
  .legend__dot--veg { background: var(--veg); }
  .legend__dot--vegan { background: var(--vegan); }
  .legend__dot--gf { background: var(--gf); }
  .legend__dot--spicy { background: var(--spicy); }

  .brand-mark {
    position: absolute; right: 14px; top: 150px;
    font-weight: 800; font-size: 15px; color: var(--gold); text-align: center; line-height: 1;
  }

  .cover__pattern {
    position: absolute; inset: 0;
    background: radial-gradient(ellipse at 40% 35%, #343434 0%, var(--cover) 60%, #1f1f1f 100%);
  }
  .cover__brand {
    position: absolute; left: 0; right: 0; top: 150px; text-align: center;
    color: var(--gold);
  }
  .cover__kicker { font-size: 8px; font-weight: 700; letter-spacing: 6px; text-transform: uppercase; }
  .cover__name { font-size: 40px; font-weight: 800; line-height: 1.05; margin: 6px 0; }
  .cover__tag { font-size: 8px; font-weight: 700; letter-spacing: 4px; text-transform: uppercase; }
  .cover__welcome {
    position: absolute; left: 30px; right: 30px; top: 300px;
    color: var(--gold); font-size: 7.4px; line-height: 1.55; text-align: center;
  }
  .cover__welcome p { margin-bottom: 3px; }
</style>
</head>
<body>

<section class="page page--left" aria-label="Food menu, left page">
  <div class="photo photo--dessert" role="img" aria-label="Photo of a Cambodian dessert on a blue plate with banana leaf"></div>
  <div class="photo photo--chicken" role="img" aria-label="Photo of grilled chicken with green papaya salad in a white bowl"></div>
  <div class="photo photo--salad" role="img" aria-label="Photo of a herb salad served on mint leaves on a white plate"></div>

  <div class="section tasty">
    <h2 class="section__title">Tasty Bites</h2>
    <div class="item"><div><div class="item__name">Betel Leaf</div><div class="item__desc">Traditional Cambodian appetiser: betel leaf with pomegranate, prawns, herbs and special sauce</div></div><div class="item__price">4.50</div></div>
    <div class="item"><div><div class="item__name">Crispy Sweet Potatoes</div><div class="item__desc">Fried finger strips of sweet potatoes served in a bowl</div></div><div class="item__price">6.00</div></div>
    <div class="item"><div><div class="item__name">Spring Rolls</div><div class="item__desc">Deep fried rolls with pork and prawns, vegetables (3 pcs)</div></div><div class="item__price">10.20</div></div>
    <div class="item"><div><div class="item__name">Vegetarian Spring Rolls</div><div class="item__desc">Deep fried rolls, vegetables (3 pcs)</div></div><div class="item__price">9.00</div></div>
    <div class="item"><div><div class="item__name">BBQ Scallop</div><div class="item__desc">Sea scallop with herbs and special house dressing (3 pcs)</div></div><div class="item__price">10.00</div></div>
    <div class="section__rule"></div>
  </div>

  <div class="section breakfast">
    <h2 class="section__title">Khmer Breakfast or Lunch</h2>
    <div class="item"><div><div class="item__name">Kuy Teav Phnom Penh</div><div class="item__desc">Traditional Cambodian noodle soup, rice and yellow noodles, choice of pork, beef or seafood</div></div><div class="item__price">15.50</div></div>
    <div class="item"><div><div class="item__name">Lot Cha</div><div class="item__desc">Rice drop noodles with Chinese chives, bean sprouts, chicken, beef ham and a dash of special sauce</div></div><div class="item__price">14.50</div></div>
    <div class="item"><div><div class="item__name">Kuy Teav Char</div><div class="item__desc">Stir-fried rice noodles, minced pork, ham, egg, bean sprouts and peanut sauce</div></div><div class="item__price">14.80</div></div>
    <div class="item"><div><div class="item__name">Lemongrass Fried Rice</div><div class="item__desc">Lemongrass, onion, chicken or beef, carrot and French beans</div></div><div class="item__price">16.50</div></div>
    <div class="section__rule"></div>
  </div>

  <div class="section house">
    <h2 class="section__title">Lotuvan Dish</h2>
    <div class="item"><div><div class="item__name">Fish Amok</div><div class="item__desc">Traditional Cambodian dish in a banana leaf. Market fish, curry paste, coconut, Chinese broccoli served with jasmine rice</div></div><div class="item__price">27.00</div></div>
    <div class="item"><div><div class="item__name">Red Curry</div><div class="item__desc">Red curry with chicken &amp; vegetable</div></div><div class="item__price">17.00</div></div>
    <div class="item"><div><div class="item__name">Green Curry</div><div class="item__desc">Green curry with beef or fish, market fish with pineapple, eggplant &amp; bamboo</div></div><div class="item__price">17.00</div></div>
    <div class="item"><div><div class="item__name">Kampot Pepper with Seafood</div><div class="item__desc">Kampot pepper with seafood, onion, carrot &amp; dash of spring onion</div></div><div class="item__price">25.00</div></div>
    <div class="item"><div><div class="item__name">Char Kreung Chicken or Fish</div><div class="item__desc">Stir-fried lemongrass chicken or fish, mix vegetables</div></div><div class="item__price">22.00</div></div>
    <div class="item"><div><div class="item__name">Beef Loc Lac</div><div class="item__desc">Cambodian marinated beef chunks and vegetable served with crispy sweet potato strips</div></div><div class="item__price">24.50</div></div>
    <div class="item"><div><div class="item__name">Traditional Lotuvan Soup</div><div class="item__desc">A mild spicy sweet and sour soup with fish &amp; mushrooms</div></div><div class="item__price">21.00</div></div>
  </div>

  <div class="legend">
    <span class="legend__item"><span class="legend__dot legend__dot--veg">V</span>Vegetarian</span>
    <span class="legend__item"><span class="legend__dot legend__dot--vegan">VE</span>Vegan</span>
    <span class="legend__item"><span class="legend__dot legend__dot--gf">G</span>Gluten free</span>
    <span class="legend__item"><span class="legend__dot legend__dot--spicy"></span>Rate of Spicy</span>
  </div>
</section>

<section class="page page--right" aria-label="Food menu, right page">
  <div class="section grill">
    <h2 class="section__title">Grill</h2>
    <div class="item"><div><div class="item__name">Beef Skewers with Papaya Salad</div><div class="item__desc">Beef skewers (4 pcs) with papaya salad served with a slice of baguette</div></div><div class="item__price">14.50</div></div>
    <div class="item"><div><div class="item__name">My Grandmothers Dish</div><div class="item__desc">Grilled chicken thighs with broken rice and tomato salad</div></div><div class="item__price">17.00</div></div>
    <div class="item"><div><div class="item__name">Grilled Corn Cob</div><div class="item__desc">Grilled corn with coconut glaze and spring onion (2 pcs)</div></div><div class="item__price">8.00</div></div>
    <div class="item"><div><div class="item__name">Old School Spareribs</div><div class="item__desc">Grilled pork ribs with mixed spices and served with carrot salad</div></div><div class="item__price">25.00</div></div>
    <div class="item"><div><div class="item__name">Grilled Pork Neck</div><div class="item__desc">Grilled pork neck with tamarind sauce, mixed salad and jasmine rice</div></div><div class="item__price">19.00</div></div>
    <div class="section__rule"></div>
  </div>

  <div class="brand-mark">Lotuvan<br>Cafe</div>

  <div class="section salads">
    <h2 class="section__title">Salads</h2>
    <div class="item"><div><div class="item__name">Glass Noodle Salad</div><div class="item__desc">With chicken or pork</div></div><div class="item__price">20.00</div></div>
    <div class="item"><div><div class="item__name">Beef Salad</div><div class="item__desc">With home made dressing &amp; herbs</div></div><div class="item__price">22.00</div></div>
    <div class="item"><div><div class="item__name">Tofu Salad</div><div class="item__desc">Mixed Asian salad with herbs &amp; coconut dressing</div></div><div class="item__price">19.50</div></div>
    <div class="section__rule"></div>
  </div>

  <div class="section sides">
    <h2 class="section__title">Side Dish</h2>
    <div class="item"><div class="item__name">Steamed Jasmine Rice</div><div class="item__price">4.00</div></div>
    <div class="item"><div class="item__name">Steamed Vegetable</div><div class="item__price">5.50</div></div>
    <div class="item"><div class="item__name">Steamed Noodle</div><div class="item__price">6.00</div></div>
    <div class="item"><div class="item__name">Rice Peanut</div><div class="item__price">4.50</div></div>
    <div class="item"><div class="item__name">Peanut Sauce</div><div class="item__price">3.00</div></div>
  </div>

  <div class="photo photo--herbs" role="img" aria-label="Photo of fresh Khmer herbs, spices and kroeung paste in a mortar"></div>
</section>

<section class="page page--cover" aria-label="Menu cover">
  <div class="cover__pattern" role="img" aria-label="Dark embossed Khmer-style swirl pattern"></div>
  <div class="cover__brand">
    <div class="cover__kicker">Traditional</div>
    <div class="cover__name">Lotuvan Cafe</div>
    <div class="cover__tag">Cambodian Cuisine</div>
  </div>
  <div class="cover__welcome">
    <p>The founder, who has a Cambodian and French background, loves to cook for people and has put a lot of patience and love to give people an understand of traditional royal food of Cambodia (Le Royal Du Cambodge).</p>
    <p>The food is made from humble beginnings and has developed into great tasting plates through our staff loving what they do, doing great work and enjoying seeing satisfied customers.</p>
    <p>Lotuvan Cafe &amp; Restaurant is committed to excellence and providing friendly welcoming service from chef to our head of Human Resources.</p>
    <p>We embrace an environment of teamwork and personal growth.</p>
    <p>Welcome to Lotuvan Cafe &amp; Restaurant!</p>
  </div>
</section>

</body>
</html>
```